Wordpress Design Project

Need a new website designed for a spin off company we own. We are a On-Site temporary housing Company specializing in rental Mobile homes, Travel trailers, and Park Models. Our clients are homeowners who are looking to do major remodeling jobs on their homes and need to move out of their home for the remodel. We bring in one of our temporary units for them to live in on their site as they remodel. WE also help people who are looking to do new home construction, and want to live on their site as they are building. This Company called " Brightmoor Dwelling Co" is a spin off of our Flagship company called Cobalt Portable Lodging (www.cobaltlodging.example) this company rents to people who have a need for on-site housing after a house fire or other disaster. Cobalt rents to Insurance company's who have a insured with a loss ( B2B). Brightmoor Dwelling Co will rent home owners directly ( B2C). We will provide you with photos for a Gallery page, and Videolinks for a video page.

Target Market(s)

people looking to rent a temporary home while they are building a home or remodeling a home

Industry/Entity Type

House

Requirements
Must have
• open - but must have a few photos that I will submit that help tell the story of hat we do.
Nice to have
• links to video we will provide -youtube vids

```html
<!DOCTYPE html>
<html lang="en">
<head>
<meta charset="utf-8">
<title>Brightmoor Dwelling Co – On-Site Temporary Housing</title>
<link href="https://fonts.googleapis.com/css2?family=Roboto+Condensed:wght@400;700&family=PT+Sans:ital,wght@0,400;0,700;1,400&display=swap" rel="stylesheet">
<style>
:root{
  --red:#d10a0a;
  --red-dark:#b30000;
  --blue:#0c4f93;
  --heading-blue:#0b4a8c;
  --text:#555;
  --btn:#5a5b5d;
  --footer:#3d3d3d;
  --band:#ececec;
  --frame:#d6d6d6;
}
*{box-sizing:border-box;margin:0;padding:0}
html,body{width:1161px;height:1200px;overflow:hidden;background:#fff}
body{font-family:"PT Sans",Arial,sans-serif;color:var(--text)}
.page{position:relative;width:1161px;height:1200px;overflow:hidden}
.abs{position:absolute}
.top-bar{left:0;top:0;width:100%;height:7px;background:var(--red)}

.brand{left:174px;top:44px;display:flex;align-items:center;gap:8px}
.brand-mark{width:22px;height:22px;background:var(--red)}
.brand-name{font-family:"Roboto Condensed",sans-serif;font-weight:700;font-size:26px;color:var(--red);text-transform:uppercase;letter-spacing:.3px;white-space:nowrap}

.phone{left:752px;top:47px;display:flex;align-items:center;gap:12px}
.phone-icon{width:36px;height:36px;border-radius:5px;background:linear-gradient(#e93a3a,#b80505);display:flex;align-items:center;justify-content:center}
.phone-text{font-family:"PT Sans",sans-serif;font-size:14px;color:#7a7a7a;white-space:nowrap}

.nav{left:174px;top:108px;width:813px;height:43px;background:var(--red);display:flex}
.nav a{display:flex;align-items:center;justify-content:center;font-family:"Roboto Condensed",sans-serif;font-weight:700;font-size:14px;color:#fff;text-decoration:none;text-transform:uppercase;white-space:nowrap}
.nav a.active{background:var(--blue)}

.hero{left:174px;top:151px;width:813px;height:332px;background:linear-gradient(180deg,#6f8063 0%,#c9c2b8 30%,#bdb5aa 70%,#7b7a70 100%)}
.hero-arrow{top:296px;width:24px;height:24px;border-radius:50%;background:rgba(60,60,60,.55);display:flex;align-items:center;justify-content:center}
.hero-caption{left:500px;top:372px;width:487px;height:92px;background:rgba(45,45,45,.82);text-align:right;padding:18px 32px 0 0;font-family:"Roboto Condensed",sans-serif;color:#fff;text-transform:uppercase;white-space:nowrap;overflow:hidden}
.hero-caption .line1{font-size:20px;line-height:26px}
.hero-caption .line2{font-size:23px;line-height:32px;font-weight:700}

h2.section{font-family:"Roboto Condensed",sans-serif;font-weight:700;font-size:17px;color:var(--red-dark);text-transform:uppercase;white-space:nowrap}
p.copy{font-size:8.7px;line-height:15px;color:var(--text)}
.btn{display:flex;align-items:center;justify-content:center;background:var(--btn);color:#e6e6e6;font-size:8.5px;text-transform:uppercase;height:25px;white-space:nowrap}

.video{left:177px;top:532px;width:222px;height:154px;background:#111;border:1px solid #333}
.video-screen{position:absolute;left:2px;top:2px;width:216px;height:131px;background:linear-gradient(180deg,#4c5a48 0%,#8d8f8c 45%,#5d605e 80%,#2b2b2b 100%)}
.video-controls{position:absolute;left:0;bottom:0;width:100%;height:19px;background:#262626;display:flex;align-items:center;padding:0 6px;gap:8px;font-size:8px;color:#ddd;white-space:nowrap}

.quote-text{left:200px;top:843px;width:200px;font-size:9.3px;line-height:15px;color:var(--text)}
.quote-name{left:175px;top:896px;font-size:9px;font-style:italic;color:var(--blue);white-space:nowrap}
.quote-mark{font-family:Georgia,serif;font-size:42px;color:#cfcfcf;line-height:1}

.subhead{font-family:"Roboto Condensed",sans-serif;font-weight:700;font-size:15px;color:var(--heading-blue);text-transform:uppercase;white-space:nowrap}
.photo-frame{border:3px solid #e6e6e6;outline:1px solid var(--frame)}
.card-head{height:31px;background:linear-gradient(#fff,#e6e6e6);font-family:"Roboto Condensed",sans-serif;font-weight:700;font-size:14px;color:var(--red-dark);padding:8px 0 0 13px;text-transform:uppercase}

.band{left:0;top:981px;width:100%;height:137px;background:linear-gradient(#e4e4e4,#f6f6f6)}
.thumb{top:998px;width:145px;height:102px;background:#fff;border:1px solid #ddd;padding:4px}
.thumb span{display:block;width:100%;height:100%}
.g-arrow{top:1043px;width:16px;height:16px;background:#d5d5d5;display:flex;align-items:center;justify-content:center}

.footer{left:0;top:1118px;width:100%;height:82px;background:var(--footer)}
.footer-brand{left:177px;top:1137px;display:flex;align-items:center;gap:8px}
.footer-brand .mark{width:26px;height:26px;border-radius:50%;border:2px solid #9a9a9a}
.footer-brand .name{font-family:"Roboto Condensed",sans-serif;font-size:17px;line-height:17px;color:#a9a9a9;text-transform:uppercase}
.footer-links{left:342px;top:1147px;display:flex;font-size:7.6px;color:#e5e5e5;text-transform:uppercase;white-space:nowrap}
.footer-links span.sep{margin:0 9px;color:#bbb}
.footer-copy{left:342px;top:1164px;font-size:7.6px;color:#d8d8d8;text-transform:uppercase;white-space:nowrap}
.badge{left:757px;top:1131px;width:56px;height:56px;border-radius:50%;background:radial-gradient(#e7c35a,#a9801f)}
.social{top:1150px;width:12px;height:12px;border-radius:50%;background:#777}
</style>
</head>
<body>
<div class="page">
  <div class="abs top-bar"></div>

  <div class="abs brand">
    <span class="brand-mark"></span>
    <span class="brand-name">Brightmoor Dwelling Co</span>
  </div>

  <div class="abs phone">
    <span class="phone-icon">
      <svg width="20" height="20" viewBox="0 0 24 24"><path fill="#fff" d="M6.6 10.8a15.1 15.1 0 0 0 6.6 6.6l2.2-2.2c.3-.3.7-.4 1-.2 1.1.4 2.3.6 3.6.6.6 0 1 .4 1 1V20c0 .6-.4 1-1 1A17 17 0 0 1 3 4c0-.6.4-1 1-1h3.5c.6 0 1 .4 1 1 0 1.3.2 2.5.6 3.6.1.3 0 .7-.2 1z"/></svg>
    </span>
    <span class="phone-text">800-555-0142 &amp; 888-555-0187</span>
  </div>

  <nav class="abs nav">
    <a class="active" style="width:91px">Home</a>
    <a style="width:121px">Services</a>
    <a style="width:124px">Floor Plans</a>
    <a style="width:113px">Gallery</a>
    <a style="width:113px">Videos</a>
    <a style="width:127px">Testimonials</a>
    <a style="width:124px">Contact Us</a>
  </nav>

  <div class="abs hero" role="img" aria-label="Photo of a beige-sided mobile home set up on a site with trees behind"></div>
  <span class="abs hero-arrow" style="left:187px"><svg width="8" height="10" viewBox="0 0 8 10"><path d="M6 1 2 5l4 4" stroke="#ddd" stroke-width="1.5" fill="none"/></svg></span>
  <span class="abs hero-arrow" style="left:951px"><svg width="8" height="10" viewBox="0 0 8 10"><path d="M2 1l4 4-4 4" stroke="#ddd" stroke-width="1.5" fill="none"/></svg></span>
  <div class="abs hero-caption">
    <div class="line1">Welcome to Cobalt Housing</div>
    <div class="line2">Your Onsite Temporary Housing Experts</div>
  </div>

  <h2 class="abs section" style="left:175px;top:502px">How It Works</h2>
  <div class="abs video">
    <div class="video-screen" role="img" aria-label="Video still of a travel trailer parked beside a house"></div>
    <svg class="abs" style="left:94px;top:50px" width="32" height="32" viewBox="0 0 32 32"><circle cx="16" cy="16" r="15" fill="#222" stroke="#999" stroke-width="1.5"/><path d="M12 9l11 7-11 7z" fill="#fff"/></svg>
    <div class="video-controls">
      <svg width="8" height="9"><rect x="0" y="0" width="3" height="9" fill="#ccc"/><rect x="5" y="0" width="3" height="9" fill="#ccc"/></svg>
      <svg width="14" height="9"><path d="M0 3h3l4-3v9L3 6H0z" fill="#888"/><rect x="9" y="3" width="1.5" height="4" fill="#888"/><rect x="12" y="1" width="1.5" height="7" fill="#888"/></svg>
      <span>0:04 / 0:30</span>
      <span style="position:relative;width:72px;height:4px;background:#111;margin-left:6px">
        <span style="position:absolute;left:0;top:0;width:12px;height:4px;background:#c00"></span>
        <span style="position:absolute;left:12px;top:0;width:34px;height:4px;background:#777"></span>
        <span style="position:absolute;left:8px;top:-3px;width:10px;height:10px;border-radius:50%;background:#ddd"></span>
      </span>
      <svg width="10" height="10" style="margin-left:auto"><path d="M0 3V0h3M7 0h3v3M10 7v3H7M3 10H0V7" stroke="#666" fill="none"/></svg>
    </div>
  </div>
  <p class="abs copy" style="left:178px;top:696px;width:225px">We have been in the On-Site Temporary Housing business for over 30 years. We have a courteous.</p>
  <span class="abs btn" style="left:177px;top:735px;width:100px">View More Videos</span>

  <h2 class="abs section" style="left:175px;top:789px">Testimonials</h2>
  <span class="abs quote-mark" style="left:174px;top:818px">&ldquo;</span>
  <p class="abs quote-text">Being able to stay at our home site was so convenient for us; we just loved "OUR" mobile home</p>
  <span class="abs quote-mark" style="left:385px;top:875px">&rdquo;</span>
  <span class="abs quote-name">R. Halvorsen, Pine Ridge MN</span>

  <h2 class="abs section" style="left:435px;top:504px;font-size:17.5px">Welcome to Cobalt Housing</h2>
  <h3 class="abs subhead" style="left:435px;top:528px">Your Onsite Temporary Housing Experts</h3>
  <p class="abs copy" style="left:435px;top:553px;width:295px">We are the leading provider of On-Site Temporary Housing. We provide Mobile Homes, Park Models and Travel Trailers. These homes are brought to your client's home site and set up. Your client can stay right at home to oversee the reconstruction.</p>
  <p class="abs copy" style="left:435px;top:628px;width:295px">We have been in the On-Site Temporary Housing business for over 30 years. We have a courteous and experienced staff.</p>
  <div class="abs photo-frame" style="left:761px;top:537px;width:225px;height:105px;background:linear-gradient(180deg,#3f72b3 0%,#8fb0d6 40%,#e9ecee 55%,#c7c9c6 75%,#6f8a3e 100%)" role="img" aria-label="Photo of a white mobile home unit on open grassland under blue sky"></div>

  <div class="abs card-head" style="left:440px;top:680px;width:260px">Services</div>
  <div class="abs photo-frame" style="left:440px;top:718px;width:260px;height:108px;background:linear-gradient(180deg,#8fb0d4 0%,#b89a74 45%,#c9a77c 70%,#8d8880 100%)" role="img" aria-label="Photo of a new house under construction with wooden roof framing"></div>
  <p class="abs copy" style="left:441px;top:838px;width:259px;text-align:justify">We provide the best On-Site Homes in the nation. Our service is second to none. We have a experienced and friendly staff. We are simply the BEST On-Site housing company.</p>
  <span class="abs btn" style="left:440px;top:896px;width:75px">Read More</span>

  <div class="abs card-head" style="left:726px;top:680px;width:261px">Floor Plans</div>
  <div class="abs photo-frame" style="left:727px;top:718px;width:260px;height:108px;background:linear-gradient(180deg,#7a5a3a 0%,#d9cfc0 35%,#9b6a33 70%,#6b3f18 100%)" role="img" aria-label="Photo of a mobile home interior kitchen with wood floor"></div>
  <p class="abs copy" style="left:728px;top:838px;width:259px;text-align:justify">We provide the best On-Site Homes in the nation. Our service is second to none. We have a experienced and friendly staff. We are simply the BEST On-Site housing company.</p>
  <span class="abs btn" style="left:726px;top:896px;width:75px">Read More</span>

  <h2 class="abs section" style="left:175px;top:951px">Gallery</h2>
  <div class="abs band"></div>
  <span class="abs g-arrow" style="left:175px"><svg width="6" height="8"><path d="M5 1 1 4l4 3" stroke="#888" fill="none"/></svg></span>
  <div class="abs thumb" style="left:197px"><span role="img" aria-label="Travel trailer parked on a driveway" style="background:linear-gradient(180deg,#6d93c9,#e8e8e8 50%,#6a8b4a)"></span></div>
  <div class="abs thumb" style="left:352px"><span role="img" aria-label="White mobile home being set on a lot" style="background:linear-gradient(180deg,#8fa3b5,#f0f0f0 55%,#6c6257)"></span></div>
  <div class="abs thumb" style="left:507px"><span role="img" aria-label="Beige mobile home on a gravel pad" style="background:linear-gradient(180deg,#5d7a4b,#cfc6b8 35%,#b6ad9f 80%,#555)"></span></div>
  <div class="abs thumb" style="left:662px"><span role="img" aria-label="Park model cabin with white front porch" style="background:linear-gradient(180deg,#d6c9a4,#c5b587 50%,#f2f2ee 80%,#7d6a48)"></span></div>
  <div class="abs thumb" style="left:818px"><span role="img" aria-label="Kitchen with wood cabinets inside a unit" style="background:linear-gradient(180deg,#c9a26b,#e2c89b 50%,#f1ede6 75%,#8d6a45)"></span></div>
  <span class="abs g-arrow" style="left:971px"><svg width="6" height="8"><path d="M1 1l4 3-4 3" stroke="#888" fill="none"/></svg></span>

  <footer class="abs footer"></footer>
  <div class="abs footer-brand"><span class="mark"></span><span class="name">Cobalt<br>Housing</span></div>
  <div class="abs footer-links">
    <span>Home</span><span class="sep">|</span><span>Services</span><span class="sep">|</span><span>Floor Plans</span><span class="sep">|</span><span>Gallery</span><span class="sep">|</span><span>Videos</span><span class="sep">|</span><span>Testimonials</span><span class="sep">|</span><span>Contact Us</span>
  </div>
  <div class="abs footer-copy">&copy; Copyright 2013. Brightmoor Dwelling Co. All rights reserved</div>
  <div class="abs badge" role="img" aria-label="Anniversary badge"></div>
  <span class="abs social" style="left:840px" aria-label="Social link"></span>
  <span class="abs social" style="left:873px" aria-label="Social link"></span>
  <span class="abs social" style="left:902px" aria-label="Social link"></span>
  <span class="abs social" style="left:935px" aria-label="Social link"></span>
  <span class="abs social" style="left:967px" aria-label="Social link"></span>
</div>
</body>
</html>
```